Moving comapny Postcard mailer Design

I am looking for a 6x9 postcard with real images of our team. I would like to add the same review we currently have , I want the colors of the postcard to be orange and white. I want the team picture to be enlarged with the other pictures to be mimized. I will add example postcards to give rough ideas. My company is called Harlow Moving and the postcards with that name are our current postcards. The additional postcards are from other companies who have better postcards than mine. My goal is for my postcard to be better that theirs.

Target Market(s)

Wealthy people in the 35+ age group

Industry/Entity Type

Moving company

Requirements
Must have
• Beauty

```html
<!DOCTYPE html>
<html lang="en">
<head>
<meta charset="utf-8">
<title>Harlow Moving – Postcard</title>
<link href="https://fonts.googleapis.com/css2?family=Montserrat:ital,wght@0,700;0,800;0,900;1,300;1,400;1,800;1,900&family=Roboto:ital,wght@0,400;1,300&display=swap" rel="stylesheet">
<style>
  :root {
    --orange: #e04e26;
    --orange-deep: #d4461f;
    --white: #ffffff;
    --ink: #2b2b2b;
    --backdrop-top: #e9e9ea;
    --backdrop-bottom: #d9d8d6;
  }
  * { box-sizing: border-box; margin: 0; padding: 0; }
  html, body { width: 1200px; height: 800px; overflow: hidden; background: var(--white); }
  .postcard {
    position: relative;
    width: 1200px;
    height: 800px;
    overflow: hidden;
    font-family: "Roboto", Arial, sans-serif;
  }
  .backdrop-photo {
    position: absolute; inset: 0;
    background: linear-gradient(160deg, var(--backdrop-top) 0%, #f1f1f1 45%, var(--backdrop-bottom) 100%);
  }
  .intro-panel {
    position: absolute;
    left: 34px; top: 27px;
    width: 1148px; height: 382px;
    background: rgba(255,255,255,0.82);
    border: 6px solid var(--white);
  }
  .headline {
    position: absolute;
    left: 82px; top: 58px;
    color: var(--orange);
    font-family: "Montserrat", Arial, sans-serif;
    font-style: italic;
    line-height: 1;
  }
  .headline-main { display: block; font-weight: 900; font-size: 96px; letter-spacing: -2px; }
  .headline-sub { display: block; font-weight: 400; font-size: 60px; margin-top: 0; letter-spacing: -1.5px; }
  .intro-copy {
    position: absolute;
    left: 79px; top: 224px;
    font-size: 17.5px;
    line-height: 23.5px;
    color: var(--ink);
    white-space: nowrap;
  }
  .team-photo {
    position: absolute;
    left: 600px; top: 33px;
    width: 578px; height: 370px;
    background: linear-gradient(135deg, #c7d3d9 0%, #4a6f73 40%, #3f5a3a 65%, #b9aa95 100%);
  }
  .route-line { position: absolute; inset: 0; pointer-events: none; }
  .coupon {
    position: absolute;
    background: var(--orange);
    color: var(--white);
    text-align: center;
  }
  .coupon::before {
    content: "";
    position: absolute;
    inset: 14px;
    border: 2px dashed rgba(255,255,255,0.9);
  }
  .coupon-small { left: 95px; top: 444px; width: 318px; height: 226px; transform: rotate(-3deg); }
  .coupon-medium { left: 449px; top: 442px; width: 307px; height: 213px; }
  .coupon-large { left: 792px; top: 446px; width: 316px; height: 222px; transform: rotate(2deg); }
  .coupon-ring { position: absolute; left: 6px; top: 16px; width: calc(100% - 12px); height: 90px; }
  .coupon-price {
    position: relative;
    margin-top: 36px;
    font-family: "Montserrat", Arial, sans-serif;
    font-weight: 900;
    font-size: 50px;
    line-height: 1;
    letter-spacing: 0.5px;
    white-space: nowrap;
  }
  .coupon-price sup { font-size: 26px; vertical-align: 18px; margin-right: 2px; }
  .coupon-terms {
    position: relative;
    margin-top: 18px;
    font-size: 30px;
    line-height: 34px;
    font-weight: 400;
    white-space: nowrap;
  }
  .coupon-note {
    position: relative;
    margin-top: 4px;
    font-size: 21px;
    font-style: italic;
    font-weight: 300;
    opacity: 0.9;
    white-space: nowrap;
  }
  .contact-band {
    position: absolute;
    left: 0; top: 687px;
    width: 1200px; height: 79px;
    background: var(--orange-deep);
    color: var(--white);
  }
  .contact-band > * {
    position: absolute;
    top: 0; height: 79px;
    display: flex; align-items: center;
    white-space: nowrap;
  }
  .contact-cta { left: 53px; font-style: italic; font-weight: 300; font-size: 30px; }
  .contact-item {
    gap: 6px;
    font-family: "Montserrat", Arial, sans-serif;
    font-weight: 800;
  }
  .contact-phone { left: 438px; font-size: 30px; }
  .contact-web { left: 770px; font-weight: 700; font-size: 28px; gap: 10px; }
  .contact-icon { width: 30px; height: 32px; flex: none; }
</style>
</head>
<body>
<main class="postcard">
  <div class="backdrop-photo" role="img" aria-label="Faded photo of movers carrying wrapped furniture outside a house"></div>

  <section class="intro-panel"></section>

  <h1 class="headline">
    <span class="headline-main">MOVING</span>
    <span class="headline-sub">MADE SIMPLE</span>
  </h1>
  <p class="intro-copy">For over ten years, our team at Harlow Moving has been<br>providing Eastern Tennessee with unparreled custom<br>moving experiences. We prioritize safety, timeliness,<br>and communication to ensure our customers are happy<br>and stress-free before, during, and after their move.<br>No matter where you need to go, we’re here to help!</p>

  <div class="team-photo" role="img" aria-label="Photo of two movers carrying a plastic-wrapped piece of furniture out of a garage"></div>

  <svg class="route-line" width="1200" height="800" viewBox="0 0 1200 800">
    <path d="M0 533 Q50 540 98 552 M190 455 Q240 410 330 406 Q420 402 480 418 Q560 436 630 420 Q700 404 760 395 Q830 360 900 330 Q1050 290 1200 268"
          fill="none" stroke="#e04e26" stroke-width="7" stroke-dasharray="18 12"/>
  </svg>

  <article class="coupon coupon-small">
    <svg class="coupon-ring" viewBox="0 0 300 90" preserveAspectRatio="none"><ellipse cx="150" cy="45" rx="146" ry="40" fill="none" stroke="#fff" stroke-width="3"/></svg>
    <p class="coupon-price"><sup>$</sup>25 OFF</p>
    <p class="coupon-terms">MOVES UNDER<br>$1000</p>
    <p class="coupon-note">With this card.</p>
  </article>

  <article class="coupon coupon-medium">
    <svg class="coupon-ring" viewBox="0 0 300 90" preserveAspectRatio="none"><ellipse cx="150" cy="45" rx="146" ry="40" fill="none" stroke="#fff" stroke-width="3"/></svg>
    <p class="coupon-price"><sup>$</sup>50 OFF</p>
    <p class="coupon-terms">MOVES UNDER<br>$1000</p>
    <p class="coupon-note">*With this card.</p>
  </article>

  <article class="coupon coupon-large">
    <svg class="coupon-ring" viewBox="0 0 300 90" preserveAspectRatio="none"><ellipse cx="150" cy="45" rx="146" ry="40" fill="none" stroke="#fff" stroke-width="3"/></svg>
    <p class="coupon-price"><sup>$</sup>100 OFF</p>
    <p class="coupon-terms">MOVES UNDER<br>$3000</p>
    <p class="coupon-note">*With this card.</p>
  </article>

  <footer class="contact-band">
    <span class="contact-cta">Call us today to get started!</span>
    <span class="contact-item contact-phone">
      <svg class="contact-icon" viewBox="0 0 24 26"><path d="M6 2 L10 7 L8 10 Q9 15 13 19 L16 17 L21 21 L18 24 Q10 24 5 15 Q2 8 6 2 Z" fill="none" stroke="#fff" stroke-width="2" stroke-linejoin="round"/></svg>
      (865) 555-0142
    </span>
    <span class="contact-item contact-web">
      <svg class="contact-icon" viewBox="0 0 26 26"><circle cx="12" cy="12" r="10" fill="none" stroke="#fff" stroke-width="2.2"/><ellipse cx="12" cy="12" rx="4.5" ry="10" fill="none" stroke="#fff" stroke-width="2"/><path d="M2 12 H22 M4 6.5 H20 M4 17.5 H14" stroke="#fff" stroke-width="2"/><path d="M15 14 L24 18 L20 19.5 L22.5 24 L20.5 25 L18 20.5 L15 23 Z" fill="#fff" stroke="#d4461f" stroke-width="1"/></svg>
      www.harlowmovers.com
    </span>
  </footer>
</main>
</body>
</html>
```